Tarrowby Builders Business Card Design

We require a business Card for a new Building Company called Tarrowby Builders. We are General Builders that specialize in Industrial, Commercial and Domestic building work. We would like to see a design that incorporates Blue ,Red and White as the colour scheme and a design that will highlight a building theme.
(Once this design is achieved will need to incorporate this for the other side of the business which is Tarrowby Joinery )

Industry/Entity Type

Business

Contact Information for Business Card

TARROWBY BUILDERS
17 Wendalee Rd Nuriootpa SA 5355
Mobile 0427390658
Telephone 08 85947316
Marcus Dewhirst
Director / Supervisor

```html
<!DOCTYPE html>
<html lang="en">
<head>
<meta charset="utf-8">
<title>Tarrowby Builders – Business Card</title>
<link rel="stylesheet" href="https://fonts.googleapis.com/css2?family=Oswald:wght@600;700&family=Lato:wght@400;700&display=swap">
<style>
  :root {
    --page-bg: #ecebe8;
    --brand-blue: #0f4f95;
    --brand-blue-deep: #0b3f7a;
    --brand-red: #c41e2a;
    --brand-red-deep: #a3141f;
    --paper: #ffffff;
    --paper-shade: #e4e4e6;
    --text-grey: #5b6470;
  }
  * { box-sizing: border-box; margin: 0; padding: 0; }
  html, body { width: 1200px; height: 1000px; overflow: hidden; }
  body {
    background: var(--page-bg);
    font-family: "Lato", Arial, sans-serif;
    position: relative;
  }
  .card {
    --accent: var(--brand-blue);
    --accent-deep: var(--brand-blue-deep);
    position: absolute;
    left: 200px;
    width: 800px;
    height: 457px;
    background: var(--paper);
    box-shadow: 0 10px 28px rgba(0,0,0,.22);
    overflow: hidden;
  }
  .card--builders { top: 28px; }
  .card--red { top: 515px; --accent: var(--brand-red); --accent-deep: var(--brand-red-deep); }

  .card__band {
    position: absolute; left: 0; top: 0;
    width: 100%; height: 278px;
    background: var(--accent);
  }
  .card__skyline {
    position: absolute; left: 0; bottom: 0;
    width: 100%; height: 150px;
    background: linear-gradient(to top, var(--accent-deep) 0%, rgba(0,0,0,0) 100%);
    opacity: .55;
  }
  .card__footer {
    position: absolute; left: 0; top: 278px;
    width: 100%; height: 179px;
    background: linear-gradient(#ffffff, var(--paper-shade));
  }

  .company-panel {
    position: absolute;
    left: 50px; top: 215px;
    width: 380px; height: 170px;
    background: linear-gradient(#ffffff, #ececee);
    box-shadow: 0 4px 14px rgba(0,0,0,.25);
    padding: 26px 28px;
  }
  .company-name {
    font-family: "Oswald", Impact, sans-serif;
    font-weight: 700;
    font-size: 34px;
    letter-spacing: .5px;
    color: var(--accent);
    line-height: 1;
    white-space: nowrap;
  }
  .company-address {
    display: flex; align-items: flex-start; gap: 12px;
    margin-top: 20px;
    font-size: 20px; line-height: 1.3;
    color: var(--accent);
  }
  .icon { width: 20px; height: 20px; flex: none; fill: var(--accent); margin-top: 3px; }

  .person {
    position: absolute; left: 465px; top: 212px;
  }
  .person__name {
    font-family: "Oswald", Impact, sans-serif;
    font-weight: 700;
    font-size: 40px;
    color: #ffffff;
    line-height: 1;
    white-space: nowrap;
  }
  .person__role {
    margin-top: 20px;
    font-size: 21px;
    color: var(--text-grey);
  }
  .contact-list {
    position: absolute; left: 500px; top: 338px;
    list-style: none;
  }
  .contact-list li {
    display: flex; align-items: center; gap: 14px;
    font-size: 22px; color: var(--accent);
    margin-bottom: 10px;
  }
  .contact-list .icon { margin-top: 0; }
</style>
</head>
<body>

<section class="card card--builders" aria-label="Tarrowby Builders business card">
  <div class="card__band">
    <div class="card__skyline" role="img" aria-label="Faint city skyline of buildings"></div>
  </div>
  <div class="card__footer"></div>

  <div class="company-panel">
    <h1 class="company-name">TARROWBY BUILDERS</h1>
    <p class="company-address">
      <svg class="icon" viewBox="0 0 20 20" aria-hidden="true"><path d="M10 1a6.5 6.5 0 0 0-6.5 6.5C3.5 12.5 10 19 10 19s6.5-6.5 6.5-11.5A6.5 6.5 0 0 0 10 1zm0 9a2.5 2.5 0 1 1 0-5 2.5 2.5 0 0 1 0 5z"/></svg>
      <span>17 Wendalee Rd Kelborough<br>SA 5391</span>
    </p>
  </div>

  <div class="person">
    <h2 class="person__name">Marcus Dewhirst</h2>
    <p class="person__role">Director / Supervisor</p>
  </div>

  <ul class="contact-list">
    <li>
      <svg class="icon" viewBox="0 0 20 20" aria-hidden="true"><rect x="1" y="1" width="18" height="18" rx="4"/><path d="M6 7c0-1.5 1.8-2 4-2s4 .5 4 2v1h-2V7H8v1H6zM6 9h8v5H6z" fill="#fff"/></svg>
      <span>08 8594 7316</span>
    </li>
    <li>
      <svg class="icon" viewBox="0 0 20 20" aria-hidden="true"><rect x="1" y="1" width="18" height="18" rx="4"/><rect x="6.5" y="4" width="7" height="12" rx="1" fill="#fff"/><rect x="7.5" y="5.5" width="5" height="8" /></svg>
      <span>0427 390 658</span>
    </li>
  </ul>
</section>

<section class="card card--red" aria-label="Tarrowby Builders business card, red version">
  <div class="card__band">
    <div class="card__skyline" role="img" aria-label="Faint city skyline of buildings"></div>
  </div>
  <div class="card__footer"></div>

  <div class="company-panel">
    <h1 class="company-name">TARROWBY BUILDERS</h1>
    <p class="company-address">
      <svg class="icon" viewBox="0 0 20 20" aria-hidden="true"><path d="M10 1a6.5 6.5 0 0 0-6.5 6.5C3.5 12.5 10 19 10 19s6.5-6.5 6.5-11.5A6.5 6.5 0 0 0 10 1zm0 9a2.5 2.5 0 1 1 0-5 2.5 2.5 0 0 1 0 5z"/></svg>
      <span>17 Wendalee Rd Kelborough<br>SA 5391</span>
    </p>
  </div>

  <div class="person">
    <h2 class="person__name">Marcus Dewhirst</h2>
    <p class="person__role">Director / Supervisor</p>
  </div>

  <ul class="contact-list">
    <li>
      <svg class="icon" viewBox="0 0 20 20" aria-hidden="true"><rect x="1" y="1" width="18" height="18" rx="4"/><path d="M6 7c0-1.5 1.8-2 4-2s4 .5 4 2v1h-2V7H8v1H6zM6 9h8v5H6z" fill="#fff"/></svg>
      <span>08 8594 7316</span>
    </li>
    <li>
      <svg class="icon" viewBox="0 0 20 20" aria-hidden="true"><rect x="1" y="1" width="18" height="18" rx="4"/><rect x="6.5" y="4" width="7" height="12" rx="1" fill="#fff"/><rect x="7.5" y="5.5" width="5" height="8" /></svg>
      <span>0427 390 658</span>
    </li>
  </ul>
</section>

</body>
</html>
```